hi all

Im after a new age looking business card with my company logo on it

must include these details, I would like the PH and Email to be symbols

If the colours used for card could be kept within the colours used in logo that I have supplied that would be great, if another colour is to be used dark grey would be ok. no light bulbs etc thanks

Details below to be incorporated on card

Damian Holloway

Lic E871302

PH 0219647381

E info@brightvaleelectrical.example.nz

Domestic Commercial Industrial Electricians

```html
<!DOCTYPE html>
<html lang="en">
<head>
<meta charset="utf-8">
<title>Brightvale Electrical – Business Card</title>
<link rel="stylesheet" href="https://fonts.googleapis.com/css2?family=Montserrat:wght@400;500;700;800&display=swap">
<style>
  :root {
    --backdrop: #e4e0da;
    --card-grey: #bababa;
    --card-white: #ffffff;
    --brand-blue: #1b75c4;
    --brand-blue-soft: #9db8dd;
    --ink: #111111;
    --muted: #7a7a7a;
  }
  * { box-sizing: border-box; margin: 0; padding: 0; }
  html, body {
    width: 1200px; height: 965px; overflow: hidden;
    background: var(--backdrop);
    font-family: "Montserrat", Arial, sans-serif;
  }
  .card {
    position: absolute; left: 278px; width: 646px; height: 368px;
    border-radius: 26px;
    box-shadow: 0 6px 14px rgba(0,0,0,0.22);
  }
  .card--front { top: 98px; background: var(--card-grey); }
  .card--back { top: 504px; background: var(--card-white); }

  .brand {
    position: absolute; display: flex; flex-direction: column; align-items: center;
    color: var(--brand-blue); font-weight: 800; text-transform: uppercase; line-height: 1;
  }
  .brand__dot {
    border-radius: 50%; background: var(--brand-blue); margin-bottom: 14px;
  }
  .card--front .brand { left: 0; right: 0; top: 70px; }
  .card--front .brand__dot { width: 58px; height: 58px; }
  .card--front .brand__name { font-size: 44px; letter-spacing: 1px; }
  .card--front .brand__sub { font-size: 30px; letter-spacing: 8px; margin-top: 8px; }

  .tagline {
    position: absolute; left: 0; right: 0; top: 322px; text-align: center;
    color: var(--brand-blue); font-weight: 700; font-size: 16.5px; letter-spacing: 0.4px;
  }

  .card--back .brand { left: 26px; width: 284px; top: 28px; }
  .card--back .brand__dot { width: 46px; height: 46px; margin-bottom: 12px; }
  .card--back .brand__name { font-size: 34px; letter-spacing: 1px; }
  .card--back .brand__sub { font-size: 23px; letter-spacing: 6px; margin-top: 6px; }

  .holder { position: absolute; right: 26px; top: 32px; text-align: right; }
  .holder__name { font-size: 25px; font-weight: 800; color: var(--ink); letter-spacing: 0.5px; }
  .holder__name .first { color: var(--brand-blue); }
  .holder__licence { font-size: 17px; color: var(--muted); margin-top: 4px; letter-spacing: 0.5px; }

  .contacts { position: absolute; left: 26px; top: 276px; list-style: none; }
  .contacts li {
    display: flex; align-items: center; gap: 10px; height: 23px;
    color: var(--brand-blue); font-size: 18px;
  }
  .contacts svg { width: 17px; height: 17px; fill: var(--brand-blue); flex: none; }

  .accent-square {
    position: absolute; right: 40px; bottom: 30px; width: 150px; height: 110px;
    background: var(--brand-blue-soft); border-radius: 4px;
  }
</style>
</head>
<body>
  <section class="card card--front">
    <div class="brand">
      <span class="brand__dot"></span>
      <span class="brand__name">Brightvale</span>
      <span class="brand__sub">Electrical</span>
    </div>
    <p class="tagline">DOMESTIC COMMERCIAL INDUSTRIAL ELECTRICIANS</p>
  </section>

  <section class="card card--back">
    <div class="brand">
      <span class="brand__dot"></span>
      <span class="brand__name">Brightvale</span>
      <span class="brand__sub">Electrical</span>
    </div>

    <div class="holder">
      <p class="holder__name"><span class="first">DAMIAN</span> HOLLOWAY</p>
      <p class="holder__licence">LIC E871302</p>
    </div>

    <ul class="contacts">
      <li>
        <svg viewBox="0 0 24 24" aria-hidden="true"><path d="M6.6 10.8a15.1 15.1 0 0 0 6.6 6.6l2.2-2.2c.3-.3.7-.4 1-.2 1.1.4 2.3.6 3.6.6.6 0 1 .4 1 1V20c0 .6-.4 1-1 1A17 17 0 0 1 3 4c0-.6.4-1 1-1h3.5c.6 0 1 .4 1 1 0 1.3.2 2.5.6 3.6.1.3 0 .7-.2 1z"/></svg>
        0219647381
      </li>
      <li>
        <svg viewBox="0 0 24 24" aria-hidden="true"><path d="M2 5h20v14H2z M2 5l10 8 10-8" fill="none" stroke="#1b75c4" stroke-width="2.4"/><path d="M2 5h20l-10 8z"/></svg>
        info@brightvaleelectrical.example.nz
      </li>
      <li>
        <svg viewBox="0 0 24 24" aria-hidden="true"><circle cx="12" cy="12" r="10"/><path d="M2 12h20M12 2c3 3 3 17 0 20M12 2c-3 3-3 17 0 20" fill="none" stroke="#fff" stroke-width="1.4"/></svg>
        www.brightvaleelectrical.example.nz
      </li>
    </ul>

    <span class="accent-square" aria-hidden="true"></span>
  </section>
</body>
</html>
```